iOS App Design Project for Pebble Notes

We are looking for a redesign of the UI for our app, Pebble Notes. The app is a to-do list type app with 4 screens, and we already have a UI for it but we would like a nicer looking one that has a better colour scheme and is more intuitive.

We would like something that is a real treat to look at, and that users really want to use. Essentially what we want is the nicest and most simple design possible, as the current UI we have is not very user friendly.

The app is already on the market and is free so if you have an iOS device you can download it and take a look at it, and we have also included screenshots of the app.
Updates

Project Deadline Extended
Reason: I am updating the design brief and will also guarantee the payment.

Target Market(s)

Mobile users looking for simplicity

Requirements
Must have
• - Very visually pleasing
- Simple layout with minimal clutter
- Icons and buttons that explain what they do
Should not have
• Any features that detract from the simplicity of the app are not wanted.

```html
<!DOCTYPE html>
<html lang="en">
<head>
<meta charset="utf-8">
<title>Pebble Notes – iOS App Screens</title>
<link href="https://fonts.googleapis.com/css2?family=Arimo:wght@400;700&family=Ubuntu+Condensed&display=swap" rel="stylesheet">
<style>
  :root{
    --board:#e4e3e4;
    --ink:#1b1d20;
    --status:#0d0d0e;
    --blue-top:#5cc3ee;
    --blue-bot:#2489c9;
    --blue-edge:#1a6fa6;
    --body:#2a2e33;
    --body-line:#30353a;
    --btn-top:#eef0f2;
    --btn-bot:#b7bec5;
    --btn-edge:#8b939b;
    --paper:#f4f4f2;
    --rule:#b9bcc0;
    --margin:#e08a8a;
    --icon-frame:#1a1c1f;
    --icon-blue-top:#2a6aa8;
    --icon-blue-bot:#163f6c;
    --label:#35383c;
  }
  *{box-sizing:border-box;margin:0;padding:0}
  html,body{width:1200px;height:1000px;overflow:hidden;background:var(--board)}
  .board{position:relative;width:1200px;height:1000px;font-family:"Arimo",Arial,sans-serif}

  .screen{position:absolute;width:311px;height:466px;overflow:hidden;
    background:repeating-linear-gradient(45deg,var(--body) 0 2px,var(--body-line) 2px 3px),var(--body)}
  .status-bar{position:absolute;left:0;top:0;width:100%;height:20px;background:var(--status);
    color:#fff;font-size:13px;font-weight:700;display:flex;align-items:center;padding:0 6px;gap:6px}
  .status-bar .signal{display:flex;align-items:flex-end;gap:1px;height:10px}
  .status-bar .signal i{display:block;width:2px;background:#fff}
  .status-bar .time{position:absolute;left:0;right:0;text-align:center}
  .status-bar .right{margin-left:auto;display:flex;align-items:center;gap:6px}
  .battery{width:20px;height:10px;border:1.5px solid #fff;border-radius:2px;padding:1px;position:relative}
  .battery::before{content:"";display:block;width:100%;height:100%;background:#fff}
  .battery::after{content:"";position:absolute;right:-4px;top:2px;width:2px;height:4px;background:#fff}
  .clock{width:10px;height:10px;border-radius:50%;background:#fff}

  .nav-bar{position:absolute;left:0;top:20px;width:100%;height:43px;
    background:linear-gradient(var(--blue-top),var(--blue-bot));border-bottom:1px solid var(--blue-edge);
    color:#fff;font-weight:700;font-size:22px;text-align:center;line-height:42px;
    text-shadow:0 -1px 0 rgba(0,0,0,.35)}
  .nav-new{position:absolute;right:8px;top:6px;width:68px;height:28px;border-radius:6px;
    background:linear-gradient(#4fb6e6,#1f7fbf);border:1px solid #17679c;font-size:16px;line-height:26px}

  .tab-bar{position:absolute;left:0;bottom:0;width:100%;height:41px;display:flex;
    background:linear-gradient(#58bde9,#2788c7);border-top:1px solid var(--blue-edge)}
  .tab{flex:1;position:relative;display:flex;flex-direction:column;align-items:center;justify-content:flex-end;
    padding-bottom:2px;color:#fff;font-size:7px;letter-spacing:.5px;border-right:1px solid rgba(0,0,0,.18)}
  .tab:last-child{border-right:0}
  .tab svg{width:22px;height:22px;margin-bottom:3px}
  .tab.is-active{background:linear-gradient(#7fd0f1,#3a9bd6);margin-top:-6px;border-radius:5px 5px 0 0;
    color:#153a5a;box-shadow:0 -1px 3px rgba(0,0,0,.4)}

  /* notes */
  .notepad{position:absolute;left:8px;top:73px;width:292px;height:305px}
  .notepad .sheet{position:absolute;left:0;width:292px;height:305px;background:var(--paper);
    border-radius:4px;box-shadow:0 1px 2px rgba(0,0,0,.5)}
  .notepad .page{top:0;background:
      linear-gradient(90deg,transparent 16px,var(--margin) 16px 17px,transparent 17px 20px,var(--margin) 20px 21px,transparent 21px),
      repeating-linear-gradient(transparent 0 21px,var(--rule) 21px 22px) 0 18px/100% 100% no-repeat,var(--paper)}
  .notepad .page p{position:absolute;left:29px;top:16px;width:240px;font-size:11px;line-height:22px;
    color:#3b3e42;letter-spacing:.6px;white-space:nowrap}
  .notepad .scroll{position:absolute;right:5px;top:14px;width:4px;height:272px;border-radius:2px;background:#c9cbce}
  .notepad .scroll::before{content:"";display:block;height:30px;border-radius:2px;background:#888}
  .ring{position:absolute;left:-6px;width:14px;height:16px;
    background:repeating-linear-gradient(#3b3e42 0 2px,transparent 2px 5px)}

  /* menu */
  .menu-stack{position:absolute;left:6px;top:95px;width:294px;height:255px}
  .menu-stack .sheet{position:absolute;background:#eceded;border-radius:3px;box-shadow:0 1px 3px rgba(0,0,0,.6)}
  .menu-row{position:absolute;left:20px;width:264px;height:42px;display:flex;align-items:center;
    font-family:"Ubuntu Condensed","Arimo",sans-serif;font-size:19px;letter-spacing:2px;color:var(--label)}
  .menu-row svg.lead{width:30px;height:30px;margin:0 20px 0 8px}
  .menu-row .chev{margin-left:auto;margin-right:16px;width:12px;height:16px}
  .menu-row.is-active{border:1px solid var(--btn-edge);border-radius:6px;background:linear-gradient(#f3f4f5,#c5cbd0)}
  .menu-row.is-active .chev-box{margin-left:auto;width:46px;height:100%;border-left:1px solid var(--btn-edge);
    display:flex;align-items:center;justify-content:center}
  .menu-divider{position:absolute;left:20px;width:264px;height:2px;background:#3a3d41;border-bottom:1px solid #fff}

  /* tasks */
  .task-btn{position:absolute;width:248px;height:35px;border-radius:5px;border:1px solid var(--btn-edge);
    background:linear-gradient(var(--btn-top),var(--btn-bot));
    font-family:"Ubuntu Condensed","Arimo",sans-serif;font-size:19px;letter-spacing:2px;color:var(--ink);
    text-align:center;line-height:33px;box-shadow:0 1px 2px rgba(0,0,0,.5);white-space:nowrap}
  .task-btn.is-selected{width:191px;height:44px;line-height:1;padding-top:7px;background:linear-gradient(#62c6ee,#2686c6);
    border-color:#17679c}
  .task-btn .date{display:block;font-size:10px;letter-spacing:1px;margin-top:3px;color:#163a5a}
  .edit-btn{position:absolute;width:39px;height:39px;border-radius:3px;background:linear-gradient(#4fb6e6,#1f7fbf);
    display:flex;align-items:center;justify-content:center}

  /* app icon placeholders */
  .app-icon{position:absolute;background:var(--icon-frame);box-shadow:0 2px 4px rgba(0,0,0,.35)}
  .app-icon .art{position:absolute;inset:8%;border-radius:14%;
    background:linear-gradient(var(--icon-blue-top),var(--icon-blue-bot))}
  .icon-caption{position:absolute;left:930px;top:548px;width:246px;text-align:center;white-space:nowrap;
    font-family:"Ubuntu Condensed","Arimo",sans-serif;font-size:30px;letter-spacing:3px;color:#2b2d30}
</style>
</head>
<body>
<div class="board">

  <svg width="0" height="0" style="position:absolute">
    <defs>
      <symbol id="i-list" viewBox="0 0 22 22"><rect x="3" y="2" width="16" height="18" rx="1" fill="none" stroke="currentColor" stroke-width="2"/><path d="M6 7h10M6 11h10M6 15h10" stroke="currentColor" stroke-width="2"/></symbol>
      <symbol id="i-task" viewBox="0 0 22 22"><rect x="2" y="3" width="17" height="17" fill="none" stroke="currentColor" stroke-width="2"/><path d="M5 11l4 4 9-11" fill="none" stroke="currentColor" stroke-width="2.2"/></symbol>
      <symbol id="i-notes" viewBox="0 0 22 22"><path d="M3 4h12v16H3z" fill="none" stroke="currentColor" stroke-width="1.6"/><path d="M5 2v4M8 2v4M11 2v4M14 2v4" stroke="currentColor" stroke-width="1.3"/><path d="M9 16l9-9 2 2-9 9-3 1z" fill="none" stroke="currentColor" stroke-width="1.5"/></symbol>
      <symbol id="i-more" viewBox="0 0 22 22"><path d="M8 2h6v6h6v6h-6v6H8v-6H2V8h6z" fill="currentColor"/></symbol>
      <symbol id="i-chev" viewBox="0 0 12 16"><path d="M2 2l7 6-7 6" fill="none" stroke="#2d3034" stroke-width="2.6"/></symbol>
    </defs>
  </svg>

  <!-- Notes screen -->
  <section class="screen screen-notes" style="left:27px;top:17px">
    <div class="status-bar"><span class="signal"><i style="height:3px"></i><i style="height:5px"></i><i style="height:7px"></i><i style="height:9px"></i></span>ORBIT&nbsp;&nbsp;3G<span class="time">4:20 PM</span><span class="right"><span class="clock"></span><span class="battery"></span></span></div>
    <header class="nav-bar">NOTES<span class="nav-new">NEW</span></header>
    <div class="notepad">
      <div class="sheet" style="top:8px;left:1px"></div>
      <div class="sheet" style="top:5px"></div>
      <div class="sheet" style="top:2px"></div>
      <div class="sheet page">
        <p>Lorem ipsum dolor sit amet, consec-<br>tetuer adipiscing elit, sed diam non-<br>ummy nibh euismod tincidunt ut lao-<br>reet dolore magna aliquam erat vo-<br>lutpat</p>
        <div class="scroll"></div>
      </div>
      <span class="ring" style="top:18px"></span>
      <span class="ring" style="top:130px"></span>
      <span class="ring" style="top:258px"></span>
    </div>
    <nav class="tab-bar">
      <div class="tab"><svg><use href="#i-list"/></svg>CALLENDER</div>
      <div class="tab"><svg><use href="#i-task"/></svg>TASK</div>
      <div class="tab is-active"><svg><use href="#i-notes"/></svg>NOTES</div>
      <div class="tab"><svg><use href="#i-more"/></svg>MORE</div>
    </nav>
  </section>

  <!-- Home menu -->
  <section class="screen screen-home" style="left:421px;top:17px">
    <div class="status-bar"><span class="signal"><i style="height:3px"></i><i style="height:5px"></i><i style="height:7px"></i><i style="height:9px"></i></span>ORBIT&nbsp;&nbsp;3G<span class="time">4:20 PM</span><span class="right"><span class="clock"></span><span class="battery"></span></span></div>
    <header class="nav-bar">PEBBLE NOTES</header>
    <div class="menu-stack">
      <div class="sheet" style="left:20px;top:28px;width:262px;height:232px;transform:rotate(1.5deg)"></div>
      <div class="sheet" style="left:8px;top:20px;width:284px;height:228px;transform:rotate(-.8deg)"></div>
      <div class="sheet" style="left:0;top:8px;width:290px;height:234px"></div>
      <div class="menu-row is-active" style="top:40px">
        <svg class="lead" viewBox="0 0 22 22" style="color:#2a8fd0"><use href="#i-task"/></svg>Task
        <span class="chev-box"><svg class="chev" style="margin:0"><use href="#i-chev"/></svg></span>
      </div>
      <div class="menu-divider" style="top:97px"></div>
      <div class="menu-row" style="top:113px">
        <svg class="lead" viewBox="0 0 22 22" style="color:#2a8fd0"><use href="#i-notes"/></svg>Notes
        <svg class="chev"><use href="#i-chev"/></svg>
      </div>
      <div class="menu-divider" style="top:167px"></div>
      <div class="menu-row" style="top:178px">
        <svg class="lead" viewBox="0 0 22 22" style="color:#2a8fd0"><use href="#i-more"/></svg>More
        <svg class="chev"><use href="#i-chev"/></svg>
      </div>
    </div>
  </section>

  <!-- Task list -->
  <section class="screen screen-tasks" style="left:22px;top:514px">
    <div class="status-bar"><span class="signal"><i style="height:3px"></i><i style="height:5px"></i><i style="height:7px"></i><i style="height:9px"></i></span>ORBIT&nbsp;&nbsp;3G<span class="time">4:20 PM</span><span class="right"><span class="clock"></span><span class="battery"></span></span></div>
    <header class="nav-bar">TASK</header>
    <div class="task-btn" style="left:31px;top:101px">Shopping</div>
    <div class="task-btn" style="left:31px;top:147px">Homework</div>
    <div class="task-btn" style="left:31px;top:193px">Task</div>
    <div class="task-btn" style="left:31px;top:239px">Task</div>
    <div class="task-btn" style="left:31px;top:285px">Task</div>
    <div class="task-btn" style="left:31px;top:331px">Task</div>
    <nav class="tab-bar">
      <div class="tab"><svg><use href="#i-list"/></svg>LIST</div>
      <div class="tab is-active"><svg><use href="#i-task"/></svg>TASK</div>
      <div class="tab"><svg><use href="#i-notes"/></svg>NOTES</div>
      <div class="tab"><svg><use href="#i-more"/></svg>MORE</div>
    </nav>
  </section>

  <!-- Task selected -->
  <section class="screen screen-tasks-edit" style="left:421px;top:514px">
    <div class="status-bar"><span class="signal"><i style="height:3px"></i><i style="height:5px"></i><i style="height:7px"></i><i style="height:9px"></i></span>ORBIT&nbsp;&nbsp;3G<span class="time">4:20 PM</span><span class="right"><span class="clock"></span><span class="battery"></span></span></div>
    <header class="nav-bar">TASK</header>
    <div class="task-btn is-selected" style="left:10px;top:100px">Shopping<span class="date">27/12/2012</span></div>
    <div class="edit-btn" style="left:216px;top:103px"><svg width="24" height="24" viewBox="0 0 24 24"><path d="M4 20l2-6L17 3l4 4-11 11z" fill="#1b2530"/></svg></div>
    <div class="task-btn" style="left:32px;top:155px">Homework</div>
    <div class="task-btn" style="left:32px;top:201px">Task</div>
    <div class="task-btn" style="left:32px;top:247px">Task</div>
    <div class="task-btn" style="left:32px;top:293px">Task</div>
    <div class="task-btn" style="left:32px;top:339px">Task</div>
    <nav class="tab-bar">
      <div class="tab"><svg><use href="#i-list"/></svg>LIST</div>
      <div class="tab is-active"><svg><use href="#i-task"/></svg>TASK</div>
      <div class="tab"><svg><use href="#i-notes"/></svg>NOTES</div>
      <div class="tab"><svg><use href="#i-more"/></svg>MORE</div>
    </nav>
  </section>

  <!-- App icon sizes -->
  <div class="app-icon" style="left:1025px;top:69px;width:63px;height:63px;border-radius:13px">
    <div class="art" role="img" aria-label="App icon artwork: notepad page with a red check mark on a blue tile"></div>
  </div>
  <div class="app-icon" style="left:1004px;top:185px;width:106px;height:106px;border-radius:21px">
    <div class="art" role="img" aria-label="App icon artwork: notepad page with a red check mark on a blue tile"></div>
  </div>
  <div class="app-icon" style="left:969px;top:340px;width:176px;height:176px;border-radius:34px">
    <div class="art" role="img" aria-label="App icon artwork: notepad page with a red check mark on a blue tile"></div>
  </div>
  <div class="icon-caption">Sample Icon</div>

</div>
</body>
</html>
```